Business card design needed

We need a business card design and possible logo for my new building construction business. I would like a masculine type of business design.

Thanks
Also can we please put my ABN number 47380926514 in as well thanks.
And use the colours black, orange and white. Cheers

Industry/Entity Type

Building

Contact Information for Business Card

Tarrow constructions, owner: Derek hollis, mobile:0417282613, email: hollo.d@quenmail.com, licence: 618374K

```html
<!DOCTYPE html>
<html lang="en">
<head>
<meta charset="utf-8">
<title>Tarrow Constructions – Business Card</title>
<link rel="stylesheet" href="https://fonts.googleapis.com/css2?family=PT+Sans:wght@400;700&family=Fjord+One&display=swap">
<style>
  :root {
    --backdrop: #cfcfcf;
    --card-white: #ffffff;
    --charcoal: #2a2c31;
    --ink: #1b1b1b;
    --orange: #e8672a;
    --muted-white: #e9e9e9;
    --stitch: #5a5d63;
  }
  * { margin: 0; padding: 0; box-sizing: border-box; }
  html, body {
    width: 1200px;
    height: 960px;
    overflow: hidden;
  }
  body {
    background: radial-gradient(circle at 50% 50%, #ececec 0%, var(--backdrop) 70%, #b9b9b9 100%);
    position: relative;
    font-family: "PT Sans", Arial, sans-serif;
  }
  .card {
    position: absolute;
    left: 300px;
    width: 600px;
    height: 367px;
    background: var(--card-white);
    box-shadow: 0 10px 28px rgba(0,0,0,0.25);
    overflow: hidden;
  }
  .card--back { top: 70px; }
  .card--front { top: 523px; }

  .card__band {
    position: absolute;
    left: 0; right: 0; bottom: 0;
    background: var(--charcoal);
  }
  .card__band::before {
    content: "";
    position: absolute;
    left: 0; right: 0; top: 0;
    height: 3px;
    background: var(--orange);
  }
  .card__band::after {
    content: "";
    position: absolute;
    left: 0; right: 0; top: 7px;
    border-top: 2px dashed var(--stitch);
  }
  .card--back .card__band { height: 70px; }
  .card--front .card__band { height: 232px; }

  /* Brand lockup */
  .brand {
    position: absolute;
    display: flex;
    align-items: center;
  }
  .brand__mark {
    background: var(--ink);
    flex: none;
  }
  .brand__name {
    color: var(--ink);
    font-weight: 400;
    white-space: nowrap;
    letter-spacing: -0.3px;
  }
  .tagline {
    position: absolute;
    color: var(--ink);
    white-space: nowrap;
  }

  .card--back .brand { left: 150px; top: 120px; gap: 16px; }
  .card--back .brand__mark { width: 26px; height: 26px; }
  .card--back .brand__name { font-size: 34px; }
  .card--back .tagline { left: 232px; top: 168px; font-size: 19px; }

  .card--front .brand { left: 38px; top: 44px; gap: 12px; }
  .card--front .brand__mark { width: 20px; height: 20px; }
  .card--front .brand__name { font-size: 27px; }
  .card--front .tagline { left: 222px; top: 83px; font-size: 15px; }

  /* Person */
  .person {
    position: absolute;
    left: 48px;
    top: 186px;
  }
  .person__name {
    font-family: "Fjord One", Georgia, serif;
    color: var(--orange);
    font-size: 25px;
    letter-spacing: 0.3px;
  }
  .person__role {
    color: var(--muted-white);
    font-size: 12px;
    text-align: right;
    margin-top: 2px;
  }

  /* Contact */
  .contact {
    position: absolute;
    left: 322px;
    top: 196px;
    list-style: none;
  }
  .contact__item {
    display: flex;
    align-items: center;
    gap: 12px;
    color: var(--muted-white);
    font-size: 13px;
    height: 24px;
  }
  .contact__icon { width: 16px; height: 16px; flex: none; }

  .registration {
    position: absolute;
    right: 34px;
    bottom: 26px;
    font-family: "Fjord One", Georgia, serif;
    color: var(--muted-white);
    font-size: 14px;
    line-height: 1.25;
  }
</style>
</head>
<body>

<section class="card card--back" aria-label="Card back">
  <div class="brand">
    <span class="brand__mark"></span>
    <span class="brand__name">Tarrow Constructions</span>
  </div>
  <span class="tagline">Solid work, honest build</span>
  <div class="card__band"></div>
</section>

<section class="card card--front" aria-label="Card front">
  <div class="brand">
    <span class="brand__mark"></span>
    <span class="brand__name">Tarrow Constructions</span>
  </div>
  <span class="tagline">Solid work, honest build</span>

  <div class="card__band"></div>

  <div class="person">
    <p class="person__name">Derek hollis</p>
    <p class="person__role">Owner</p>
  </div>

  <ul class="contact">
    <li class="contact__item">
      <svg class="contact__icon" viewBox="0 0 24 24" aria-hidden="true">
        <path fill="#e8672a" d="M6.6 10.8c1.4 2.8 3.8 5.1 6.6 6.6l2.2-2.2c.3-.3.7-.4 1-.2 1.1.4 2.3.6 3.6.6.6 0 1 .4 1 1V20c0 .6-.4 1-1 1C10.6 21 3 13.4 3 4c0-.6.4-1 1-1h3.5c.6 0 1 .4 1 1 0 1.3.2 2.5.6 3.6.1.3 0 .7-.2 1l-2.3 2.2z"/>
      </svg>
      <span>0417282613</span>
    </li>
    <li class="contact__item">
      <svg class="contact__icon" viewBox="0 0 24 24" aria-hidden="true">
        <path fill="#e8672a" d="M2 5h20v14H2z"/>
        <path fill="none" stroke="#2a2c31" stroke-width="1.8" d="M2.5 5.5l9.5 7.5 9.5-7.5"/>
      </svg>
      <span>hollo.d@quenmail.com</span>
    </li>
  </ul>

  <p class="registration">ABN: 47380926514<br>licence: 618374K</p>
</section>

</body>
</html>
```